Addiction Treatment and Mental Health Center needs a brochure

Our company is called, Willowmere House Islamabad, and it is a private, upscale addiction recovery and mental health facility that provides comprehensive client-centred treatment and support for individuals and their families. We provide both short-term and long-term residential treatment, outpatient services, continuing care, and family support. We strive to offer the highest quality standards of care through implementing innovative and evidence-based treatment programs, quality control measures, and ethical decision making protocols. Our treatment style is holistic and incorporates modern medicine and therapies along with complimentary and alternative healing therapies. We also distinguish ourselves by offering a treatment environment that is open, green and and serene. We would like to see a brochure design that reflects these elements and our approach to treatment.
Requirements
Must have
- Tri-fold pamphlet

```html
<!DOCTYPE html>
<html lang="en">
<head>
<meta charset="utf-8">
<title>Willowmere House Islamabad – Our Program of Recovery</title>
<link href="https://fonts.googleapis.com/css2?family=Roboto+Condensed:ital,wght@0,300;0,400;0,700;1,400;1,700&display=swap" rel="stylesheet">
<style>
  :root {
    --blue: #0b5da6;
    --blue-rule: #3f7fc0;
    --green: #1d6a2f;
    --ink: #2e2e2e;
    --white: #ffffff;
    --amber: #c97a2a;
    --amber-dark: #a35d18;
  }
  * { margin: 0; padding: 0; box-sizing: border-box; }
  html, body { width: 1200px; height: 932px; overflow: hidden; background: var(--white); }
  body { font-family: "Roboto Condensed", "Arial Narrow", sans-serif; color: var(--ink); }
  .brochure { position: relative; width: 1200px; height: 932px; overflow: hidden; }

  .hero {
    position: absolute; left: 0; top: 0; width: 797px; height: 530px;
    background:
      radial-gradient(ellipse 45% 55% at 58% 0%, rgba(230,255,200,.75), rgba(230,255,200,0) 70%),
      radial-gradient(ellipse 80% 70% at 50% 35%, #5fbf3e, #2f8a2c 60%, #1d4a1d 100%);
  }
  .hero-shade {
    position: absolute; left: 0; bottom: 0; width: 100%; height: 45%;
    background: linear-gradient(to bottom, rgba(10,30,12,0), rgba(10,30,12,.55));
  }
  .hero-band {
    position: absolute; left: 0; top: 530px; width: 797px; height: 11px;
    background: linear-gradient(to right, var(--amber-dark), var(--amber), var(--amber-dark));
  }
  .brand-mark {
    position: absolute; left: 28px; top: 431px; width: 109px; height: 109px;
    border-radius: 50%; background: var(--white);
    display: flex; align-items: center; justify-content: center; text-align: center;
    font-size: 14px; font-weight: 700; color: var(--blue); line-height: 1.1;
  }
  .hero-title {
    position: absolute; left: 147px; top: 440px;
    color: var(--white); font-weight: 400; font-size: 38px; line-height: 38px; letter-spacing: .3px;
  }
  .hero-title .small { font-size: 28px; }

  .intro {
    position: absolute; left: 35px; top: 561px; width: 345px;
    font-size: 16.4px; line-height: 19.8px; font-weight: 400;
  }
  .intro p + p { margin-top: 19.8px; }

  .treatments { position: absolute; left: 432px; top: 559px; width: 345px; }
  .lead-green {
    color: var(--green); font-style: italic; font-weight: 700; font-size: 17.8px; line-height: 21.8px;
  }
  .bullet-list { list-style: none; margin-top: 12px; }
  .bullet-list li {
    position: relative; padding-left: 20px; font-size: 17px; line-height: 20px; height: 37.6px;
  }
  .bullet-list li::before {
    content: ""; position: absolute; left: 1px; top: 5px; width: 10px; height: 10px;
    border-radius: 50%; background: var(--green);
  }
  .note-green {
    position: absolute; left: 431px; top: 840px; width: 350px;
    color: var(--green); font-style: italic; font-weight: 700; font-size: 16px; line-height: 19.8px;
  }

  .offer {
    position: absolute; left: 797px; top: 0; width: 403px; height: 932px;
    background: var(--blue); color: var(--white);
  }
  .offer h2 {
    position: absolute; left: 29px; top: 38px; font-weight: 400; font-size: 37px; line-height: 40px; letter-spacing: .3px;
  }
  .offer-lead {
    position: absolute; left: 28px; top: 92px; width: 360px;
    font-style: italic; font-weight: 700; font-size: 16px; line-height: 19.8px;
  }
  .check-list { position: absolute; left: 29px; top: 240px; width: 345px; list-style: none; }
  .check-list li {
    position: relative; height: 37.6px; padding-left: 26px; padding-top: 5px;
    font-size: 17px; font-weight: 700; line-height: 20px;
  }
  .check-list li:not(:last-child)::after {
    content: ""; position: absolute; left: 26px; right: 0; bottom: 0; height: 1px;
    background: var(--blue-rule);
  }
  .check-list svg { position: absolute; left: 0; top: 3px; width: 21px; height: 19px; }
  .offer-body {
    position: absolute; left: 32px; top: 507px; width: 345px;
    font-size: 16px; line-height: 19.8px; font-weight: 400;
  }
  .offer-body p + p { margin-top: 19.8px; }
</style>
</head>
<body>
<main class="brochure">
  <section class="hero" role="img" aria-label="Photograph of a support group holding hands in a circle, bathed in green light">
    <div class="hero-shade"></div>
  </section>
  <div class="hero-band"></div>
  <div class="brand-mark">Willowmere<br>House</div>
  <h1 class="hero-title">OUR PROGRAM<br><span class="small">OF</span> RECOVERY</h1>

  <section class="intro">
    <p>At Willowmere House, we believe recovery is multidirectional. Our teams of professional medical experts and therapist design a holistic approach customized to cater to the needs of each patient in need of alcoholism treatment in Islamabad.</p>
    <p>We take inspiration from world-renowned therapists and rehab specialists; because of which, the systems at Willowmere House have been producing positive results consistently. When we design rehabilitation programs for the clients, our focus is on all aspect of life such as physical, psychological, social and mental. To overcome the difficulties during withdrawal, we offer round the clock services for all our clients receiving treatment at the facility or at home.</p>
  </section>

  <section class="treatments">
    <p class="lead-green">We offer drug treatment in Islamabad for substance abuse addicts dealing with cocaine, tobacco, heroin, meth and prescription drugs addictions.</p>
    <ul class="bullet-list">
      <li>EDUCATIONAL GROUPS AND LECTURES</li>
      <li>ACCEPTANCE AND COMMITMENT THERAPY</li>
      <li>MINDFULNESS-BASED COGNITIVE THERAPY</li>
      <li>DIALECTICAL BEHAVIORAL THERAPY</li>
      <li>COGNITIVE BEHAVIORAL THERAPY</li>
    </ul>
  </section>
  <p class="note-green">Our certified medical team of experts is qualified to treat different mental health conditions which may require admission in the rehab center.</p>

  <aside class="offer">
    <h2>WHAT WE OFFER</h2>
    <p class="offer-lead">We offer detox programs for drug and alcohol addicts in Pakistan. Our medical teams are professionals experienced to treat mental health patients, substance abuse and alcohol addicts. We offer customized treatment approaches according to the individual patients’ needs.</p>
    <ul class="check-list">
      <li><svg viewBox="0 0 21 19"><path d="M1 10 L7 16 L20 1" fill="none" stroke="#fff" stroke-width="3.5" stroke-linecap="round" stroke-linejoin="round"/></svg>MEDICAL DETOXIFICATION</li>
      <li><svg viewBox="0 0 21 19"><path d="M1 10 L7 16 L20 1" fill="none" stroke="#fff" stroke-width="3.5" stroke-linecap="round" stroke-linejoin="round"/></svg>INPATIENT TREATMENT</li>
      <li><svg viewBox="0 0 21 19"><path d="M1 10 L7 16 L20 1" fill="none" stroke="#fff" stroke-width="3.5" stroke-linecap="round" stroke-linejoin="round"/></svg>OUTPATIENT TREATMENT</li>
      <li><svg viewBox="0 0 21 19"><path d="M1 10 L7 16 L20 1" fill="none" stroke="#fff" stroke-width="3.5" stroke-linecap="round" stroke-linejoin="round"/></svg>EDUCATIONAL GROUPS AND LECTURES</li>
      <li><svg viewBox="0 0 21 19"><path d="M1 10 L7 16 L20 1" fill="none" stroke="#fff" stroke-width="3.5" stroke-linecap="round" stroke-linejoin="round"/></svg>ACCEPTANCE AND COMMITMENT THERAPY</li>
      <li><svg viewBox="0 0 21 19"><path d="M1 10 L7 16 L20 1" fill="none" stroke="#fff" stroke-width="3.5" stroke-linecap="round" stroke-linejoin="round"/></svg>DIALECTICAL BEHAVIORAL THERAPY (DBT)</li>
    </ul>
    <div class="offer-body">
      <p>Our expanded network of outpatient services is accessible to recovering addicts all over Pakistan. This is designed to motivate our clients to go back to regular life and involve in various activities without the fear of a relapse.</p>
      <p>We use various emotional approaches for treatment such as cognitive behavioral theory and a special focus on nutrition. The addicts’ physical health is maintained with proper nutrition and medication if needed.</p>
      <p>When discharging the patient from the Willowmere House rehab in Islamabad, family counseling is encouraged to make sure the loved ones of our patient are well informed about how to maintain a positive environment that is vital for long term success of treatment.</p>
    </div>
  </aside>
</main>
</body>
</html>
```